Brindle Logistics Business Card Design

We are a trucking and warehousing company. We run freight in the US manly from the Pacific NW to TX and back up the the PNW. We also do warehousing where we store, move, and distribute freight. Looking for a clean and modern design of business card. We would like to look rich and elegant. Attached is our logo.

Industry/Entity Type

Trucking Company

Contact Information for Business Card

Looking for a clean and modern design of business card. We would like to look rich and elegant.

Font styles to use
Sans Serif

Colors

Designer to choose colors to be used in the design.

Requirements
Must have
• logo but it should not dominate the card
Should not have
• logo should not dominate the card

```html
<!DOCTYPE html>
<html lang="en">
<head>
<meta charset="utf-8">
<title>Brindle Logistics – Business Card</title>
<link href="https://fonts.googleapis.com/css2?family=Arimo:wght@400&family=Tinos:wght@400&display=swap" rel="stylesheet">
<style>
  :root {
    --page: #f4f4f4;
    --blue: #1679c4;
    --blue-deep: #0f72bb;
    --blue-light: #3a92d2;
    --orange: #f7941d;
    --white: #ffffff;
    --ink: #1f2a44;
  }
  html, body {
    margin: 0;
    padding: 0;
    width: 1200px;
    height: 1200px;
    overflow: hidden;
    background: var(--page);
  }
  .canvas {
    position: relative;
    width: 1200px;
    height: 1200px;
  }
  .card {
    position: absolute;
    left: 270px;
    width: 824px;
    height: 470px;
    transform: scale(0.8);
    transform-origin: top left;
    overflow: hidden;
  }
  .card--front { top: 154px; background: var(--blue); }
  .card--back  { top: 668px; background: var(--white); }
  .card svg.shapes {
    position: absolute;
    inset: 0;
    width: 824px;
    height: 470px;
  }

  /* front */
  .front-title {
    position: absolute;
    right: 72px;
    top: 142px;
    margin: 0;
    text-align: left;
    color: var(--white);
    font-family: "Arimo", Arial, sans-serif;
    font-weight: 400;
    line-height: 1;
  }
  .front-title__name {
    display: block;
    font-size: 78px;
    letter-spacing: 1px;
  }
  .front-title__sub {
    display: block;
    margin-top: 14px;
    font-size: 36px;
  }

  /* back */
  .back-heading {
    position: absolute;
    right: 110px;
    top: 68px;
    margin: 0;
    font-family: "Tinos", "Times New Roman", serif;
    font-weight: 400;
    font-size: 38px;
    color: var(--blue-deep);
    white-space: nowrap;
  }
  .back-tagline {
    position: absolute;
    right: 106px;
    top: 140px;
    margin: 0;
    font-family: "Tinos", "Times New Roman", serif;
    font-size: 20px;
    color: var(--orange);
    white-space: nowrap;
  }
  .contact-list {
    position: absolute;
    left: 470px;
    top: 264px;
    margin: 0;
    padding: 0;
    list-style: none;
    font-family: "Tinos", "Times New Roman", serif;
    font-size: 20px;
    color: var(--white);
  }
  .contact-list li {
    display: flex;
    align-items: center;
    height: 30px;
  }
  .contact-list svg {
    width: 16px;
    height: 16px;
    margin-right: 22px;
    fill: var(--white);
  }
  .brand-mark {
    position: absolute;
    left: 26px;
    top: 386px;
    display: flex;
    align-items: center;
    gap: 10px;
    font-family: "Tinos", "Times New Roman", serif;
    font-size: 19px;
    line-height: 1.1;
    color: var(--blue-deep);
  }
  .brand-mark__dot {
    width: 38px;
    height: 38px;
    border-radius: 50%;
    background: var(--blue-deep);
  }
</style>
</head>
<body>
<main class="canvas">

  <section class="card card--front" aria-label="Business card front">
    <svg class="shapes" viewBox="0 0 824 470">
      <defs>
        <linearGradient id="mapTone" x1="0" y1="0" x2="1" y2="1">
          <stop offset="0" stop-color="#3c95d4"/>
          <stop offset="0.5" stop-color="#1f80c8"/>
          <stop offset="1" stop-color="#1574be"/>
        </linearGradient>
      </defs>
      <rect class="map-area" role="img" aria-label="Faint map of the United States behind the card face" x="0" y="0" width="824" height="470" fill="url(#mapTone)"/>
      <rect class="map-band" x="0" y="0" width="824" height="63" fill="#ffffff" opacity="0.08"/>
      <polygon class="stripe-main" points="0,0 100,0 417,470 205,470 0,164" fill="var(--orange)"/>
      <polygon class="stripe-edge" points="0,224 165,470 130,470 0,276" fill="var(--orange)"/>
      <polygon class="stripe-thin" points="137,0 162,0 309,228 284,228" fill="var(--orange)"/>
      <polygon class="stripe-thin" points="182,0 207,0 354,228 329,228" fill="var(--orange)"/>
    </svg>
    <h1 class="front-title">
      <span class="front-title__name">BRINDLE</span>
      <span class="front-title__sub">LOGISTICS LLC</span>
    </h1>
  </section>

  <section class="card card--back" aria-label="Business card back">
    <svg class="shapes" viewBox="0 0 824 470">
      <polygon class="panel-blue" points="293,180 824,180 824,470 492,470" fill="var(--blue-deep)"/>
      <polygon class="stripe-thin" points="50,131 80,131 312,470 282,470" fill="var(--orange)"/>
      <polygon class="stripe-main" points="108,131 260,131 492,470 340,470" fill="var(--orange)"/>
      <polygon class="stripe-thin" points="287,131 312,131 428,300 403,300" fill="var(--orange)"/>
      <polygon class="stripe-thin" points="322,131 352,131 468,300 438,300" fill="var(--orange)"/>
      <line class="divider" x1="485" y1="127" x2="716" y2="127" stroke="var(--ink)" stroke-width="1.5"/>
      <rect class="divider-accent" x="485" y="124" width="38" height="6" fill="var(--orange)"/>
    </svg>

    <h2 class="back-heading">Brindle Logistics LLC</h2>
    <p class="back-tagline">Trucking and warehousing company</p>

    <ul class="contact-list">
      <li>
        <svg viewBox="0 0 16 16" aria-hidden="true"><path d="M8 0a5.5 5.5 0 0 0-5.5 5.5C2.5 9.6 8 16 8 16s5.5-6.4 5.5-10.5A5.5 5.5 0 0 0 8 0zm0 7.8a2.3 2.3 0 1 1 0-4.6 2.3 2.3 0 0 1 0 4.6z"/></svg>
        Halvern , Westmark
      </li>
      <li>
        <svg viewBox="0 0 16 16" aria-hidden="true"><path d="M3.6 0.5l2.3 3.1-1.5 2a9.5 9.5 0 0 0 6 6l2-1.5 3.1 2.3-1.4 2.8C8 15 1 8 0.8 1.9z"/></svg>
        +00 271 908 346 512
      </li>
      <li>
        <svg viewBox="0 0 16 16" aria-hidden="true"><path d="M0 3h16v1.2L8 9 0 4.2zM0 5.8l8 4.8 8-4.8V13H0z"/></svg>
        info@brindlelogistics
      </li>
      <li>
        <svg viewBox="0 0 16 16" aria-hidden="true"><path d="M3 0l10 9.5H8.2l2.6 5.3-2 1-2.6-5.4L3 13.5z"/></svg>
        www.brindlelogistics.com
      </li>
    </ul>

    <div class="brand-mark">
      <span class="brand-mark__dot"></span>
      <span class="brand-mark__name">BRINDLE<br>LOGISTICS, LLC</span>
    </div>
  </section>

</main>
</body>
</html>
```